Ray's Personal Training -> also needs a logo

Services Frankston, Mornington, and Somerville

Specializes in in-home personal training

VimTrek style workouts

Not really preferential colors but needs to look modern and not stock photo

Industry/Entity Type

Training

Requirements
Must have
• 30% off first time customers on a package of 10

```html
<!DOCTYPE html>
<html lang="en">
<head>
<meta charset="utf-8">
<title>Ray's Personal Training</title>
<link rel="stylesheet" href="https://fonts.googleapis.com/css2?family=Open+Sans:wght@700&family=Libre+Franklin:wght@700&family=Questrial&display=swap">
<style>
  :root {
    --bg-top: #e4e7e7;
    --bg-mid: #ffffff;
    --bg-low: #d9dede;
    --ink: #3a3f40;
    --corner: #353a3a;
    --corner-ink: #d9dddd;
  }
  * { margin: 0; padding: 0; box-sizing: border-box; }
  html, body { width: 1200px; height: 900px; overflow: hidden; }
  .flyer {
    position: relative;
    width: 1200px;
    height: 900px;
    background: linear-gradient(180deg, var(--bg-top) 0%, var(--bg-mid) 30%, var(--bg-mid) 55%, var(--bg-low) 100%);
    color: var(--ink);
    overflow: hidden;
  }
  .brand {
    position: absolute;
    left: 0; right: 0;
    top: 248px;
    text-align: center;
    font-family: "Open Sans", sans-serif;
    font-weight: 700;
    color: var(--ink);
  }
  .brand-name {
    display: block;
    font-size: 236px;
    line-height: 1;
    letter-spacing: 2px;
    margin-left: 20px;
  }
  .brand-line {
    display: block;
    font-size: 60px;
    line-height: 1;
    margin-left: 40px;
  }
  .brand-line.first { margin-top: 88px; }
  .brand-line.second { margin-top: 2px; }
  .details {
    position: absolute;
    left: 45px;
    top: 586px;
  }
  .details-heading {
    font-family: "Libre Franklin", sans-serif;
    font-weight: 700;
    font-size: 36px;
    line-height: 1;
  }
  .details-list {
    list-style: none;
    font-family: "Questrial", sans-serif;
    line-height: 1.05;
  }
  .areas { font-size: 29px; margin-top: 3px; }
  .areas .narrow { font-size: 24px; }
  .specialties-heading { margin-top: 10px; }
  .specialties { font-size: 38px; margin-top: 6px; line-height: 1.14; }
  .offer-corner {
    position: absolute;
    left: 0; top: 0;
  }
  .offer {
    position: absolute;
    right: 35px;
    top: 622px;
    width: 305px;
    text-align: right;
    color: var(--corner-ink);
  }
  .offer-amount {
    font-family: "Questrial", sans-serif;
    font-size: 78px;
    line-height: 0.95;
  }
  .offer-rule {
    height: 2px;
    background: var(--corner-ink);
    margin: 12px 0 14px;
  }
  .offer-terms {
    font-family: "Libre Franklin", sans-serif;
    font-weight: 700;
    font-size: 23px;
    line-height: 1.5;
  }
</style>
</head>
<body>
<main class="flyer">
  <svg class="offer-corner" width="1200" height="900" viewBox="0 0 1200 900" aria-hidden="true">
    <polygon points="1200,415 1200,900 703,900" fill="var(--corner)"/>
  </svg>

  <h1 class="brand">
    <span class="brand-name">RAYS</span>
    <span class="brand-line first">PERSONAL</span>
    <span class="brand-line second">TRAINING</span>
  </h1>

  <section class="details">
    <h2 class="details-heading">SERVICES:</h2>
    <ul class="details-list areas">
      <li>FRANKSTON</li>
      <li class="narrow">MORNINGTON</li>
      <li>SOMERVILLE</li>
    </ul>
    <h2 class="details-heading specialties-heading">SPECIALIZES IN:</h2>
    <ul class="details-list specialties">
      <li>IN-HOME PERSONAL TRAINING</li>
      <li>VIMTREK STYLE WORKOUTS</li>
    </ul>
  </section>

  <section class="offer">
    <p class="offer-amount">30%<br>OFF</p>
    <div class="offer-rule"></div>
    <p class="offer-terms">first time customers<br>on a package of 10</p>
  </section>
</main>
</body>
</html>
```